KOVA WIRING PTE LTD
KOVA WIRING NAME CARD
Project: KOVA WIRING PTE LTD
KOVA WIRING PTE LTD - Engineering
Creative Brief
Professional
Deren Whitcombe
Manager
57 Tannery Lane #03-22 Silverbrook Industrial Complex Singapore 347912
derenkovawiring@mailbox-example.net
Reg No. 198733502K
https://www.filevault-example.net/share/7qe2kx9/ZTRmPwq4HnLc?dl=0 Pleas find folder for the logo design A.I. file. Thanks Client love the 3 colour in the logo design for FengShui purposes.
harlowbek harlowbek
Hi my client like your design #218, Can you give the stationary set for #218. We try to finalize by tomorrow. Thanks

```html
<!DOCTYPE html>
<html lang="en">
<head>
<meta charset="utf-8">
<title>KOVA WIRING — Name Card</title>
<link href="https://fonts.googleapis.com/css2?family=Jost:wght@400;500;600&display=swap" rel="stylesheet">
<style>
  :root {
    --bg: #e9e7e3;
    --card-black: #0b0b0b;
    --card-white: #ffffff;
    --ink: #2b2b2b;
    --muted: #6a6a6a;
    --green: #17a05a;
    --navy: #2c2a6b;
  }
  * { margin: 0; padding: 0; box-sizing: border-box; }
  html, body {
    width: 1200px; height: 904px; overflow: hidden;
    background: var(--bg);
    font-family: "Jost", sans-serif;
  }
  .stage {
    width: 1200px; height: 904px;
    display: flex; flex-direction: column;
    align-items: center; justify-content: center; gap: 40px;
  }
  .card {
    width: 700px; height: 400px;
    position: relative; overflow: hidden;
    box-shadow: 0 6px 18px rgba(0,0,0,.18);
  }
  /* back side */
  .card--back {
    background: var(--card-black);
    display: flex; align-items: center; justify-content: center;
  }
  .brand {
    display: flex; align-items: center; gap: 14px;
  }
  .brand__square {
    width: 34px; height: 34px; background: var(--green);
  }
  .brand__name {
    font-weight: 600; font-size: 30px; letter-spacing: 2px;
  }
  .card--back .brand__name { color: #ffffff; }

  /* front side */
  .card--front { background: var(--card-white); }
  .front__band {
    position: absolute; left: 0; top: 0; bottom: 0; width: 120px;
    background: var(--card-black);
  }
  .front__brand {
    position: absolute; left: 96px; top: 92px;
  }
  .front__brand .brand__square { width: 48px; height: 48px; }
  .front__brand .brand__name { color: var(--ink); font-size: 34px; }
  .person {
    position: absolute; left: 180px; top: 220px;
  }
  .person__name { color: var(--green); font-size: 19px; font-weight: 500; }
  .person__role { color: var(--muted); font-size: 12px; margin-top: 2px; }
  .contact {
    position: absolute; left: 440px; top: 150px;
    color: var(--ink); font-size: 12.5px; line-height: 1.4;
  }
  .contact__address { margin-bottom: 14px; }
  .contact__list { list-style: none; }
  .contact__list li { display: flex; align-items: center; gap: 8px; }
  .contact__list svg { width: 12px; height: 12px; flex: none; }
</style>
</head>
<body>
<main class="stage">
  <section class="card card--back" aria-label="Card back">
    <div class="brand">
      <span class="brand__square"></span>
      <span class="brand__name">KOVA WIRING</span>
    </div>
  </section>

  <section class="card card--front" aria-label="Card front">
    <div class="front__band"></div>
    <div class="brand front__brand">
      <span class="brand__square"></span>
      <span class="brand__name">KOVA WIRING</span>
    </div>
    <div class="person">
      <p class="person__name">Deren Whitcombe</p>
      <p class="person__role">Manager</p>
    </div>
    <div class="contact">
      <p class="contact__address">57 Tannery Lane<br>#03-22 Silverbrook Industrial Complex<br>Singapore 347912</p>
      <ul class="contact__list">
        <li><svg viewBox="0 0 12 12"><path fill="#17a05a" d="M2 1h2.5l1 2.5-1.3 1a6 6 0 0 0 3.3 3.3l1-1.3 2.5 1V11A10 10 0 0 1 1 2z"/></svg>(65) 61230487</li>
        <li><svg viewBox="0 0 12 12"><rect x="3" y="0.5" width="6" height="11" rx="1" fill="#17a05a"/><rect x="4" y="2" width="4" height="6.5" fill="#fff"/></svg>(65) 90417256</li>
        <li><svg viewBox="0 0 12 12"><rect x="1" y="4" width="10" height="6" fill="#17a05a"/><rect x="3" y="1" width="6" height="3" fill="#17a05a"/><rect x="3" y="6" width="6" height="1" fill="#fff"/></svg>(65) 61230487</li>
        <li><svg viewBox="0 0 12 12"><rect x="0.5" y="2" width="11" height="8" fill="#17a05a"/><path d="M1 2.5l5 4 5-4" fill="none" stroke="#fff" stroke-width="1"/></svg>derenkovawiring@mailbox-example.net</li>
      </ul>
    </div>
  </section>
</main>
</body>
</html>
```